Banner for Vet Hospital 5m x 1.2m - Heat Stroke

Maplecourt Pet Hospital needs a Heat Stroke Banner for Summer.
The banner will be 5000mm long and 1200mm tall.

Our region has been hot this year and this summer is going to be extremely hot.
I want to warn people about heat stroke.
I want you to create a heat stroke banner that conveys the symptoms of heat stroke.

Pictures are better than words.
There should be IMAGES and WORDS that can be seen from the road 30m away and maybe some smaller words for people to read as they walk past.

Here are some of the signs of Heat Stroke:
- Panting which increases as heatstroke progresses
- Drooling, salivating
- Agitation, restlessness
- Very red or pale gums
- Bright red tongue
- Increased heart rate
- Breathing distress
- Vomiting Diarrhea (possibly with blood)
- Signs of mental confusion, delirium
- Dizziness, staggering
- Lethargy, weakness
- Muscle tremors
- Seizures
- Collapsing and lying down
- Little to no urine production
- Coma

I have attached characters that we often use in our advertising. They are optional.
I have done a mock up of the design I imagine. You could refine this design or make your own....or both.

Target Market(s)

Women aged 20 to 50.

Industry/Entity Type

Veterinary

Font styles to use
Sans Serif

Colors
fbed22
f78f20
ec1f27
ffffff

Requirements
Must have
• Heat Stroke Symtpms.
• Heat Stroke Warning.
• Summer theme.
Nice to have
• Bright colours.

```html
<!DOCTYPE html>
<html lang="en">
<head>
<meta charset="utf-8">
<title>Maplecourt Pet Hospital – Heat Stroke Banner</title>
<link href="https://fonts.googleapis.com/css2?family=Archivo+Black&family=Berkshire+Swash&family=Roboto:wght@500;700&display=swap" rel="stylesheet">
<style>
  :root {
    --sun-yellow: #fbed22;
    --summer-orange: #f78f20;
    --alert-red: #ec1f27;
    --white: #ffffff;
    --ink: #111111;
    --stage: #e4e4e4;
    --brand-brown: #5a4636;
    --photo-top: #d3e3ea;
    --photo-bottom: #eadfcf;
  }
  * { margin: 0; padding: 0; box-sizing: border-box; }
  html, body {
    width: 1200px; height: 1200px; overflow: hidden;
    background: var(--stage);
    font-family: "Roboto", Arial, sans-serif;
  }
  .banner {
    position: absolute; left: 30px; top: 463px;
    width: 1335px; height: 320px;
    transform: scale(0.854); transform-origin: 0 0;
    overflow: hidden;
    background: var(--white);
    box-shadow: 0 6px 18px rgba(0,0,0,.18);
  }
  .banner-shapes { position: absolute; inset: 0; }
  .text { position: absolute; white-space: nowrap; }

  .question {
    left: 641px; top: 34px;
    font-family: "Berkshire Swash", cursive;
    font-size: 27px; color: var(--white);
  }
  .symptom {
    font-family: "Berkshire Swash", cursive;
    font-size: 20px; color: var(--sun-yellow);
    display: flex; align-items: center; gap: 8px;
  }
  .symptom svg { width: 16px; height: 16px; fill: var(--white); }

  .headline {
    left: 843px; top: 30px;
    font-family: "Archivo Black", sans-serif;
    font-size: 32px; color: var(--ink); letter-spacing: .5px;
  }
  .tagline {
    font-weight: 700; font-size: 15.5px; color: var(--summer-orange);
    line-height: 18px;
  }
  .get-to-know { left: 815px; top: 130px; font-weight: 700; font-size: 15px; color: var(--ink); }
  .topics {
    left: 808px; top: 150px;
    display: flex; gap: 14px;
    font-weight: 700; font-size: 15px; color: var(--ink);
  }
  .topics span { display: flex; align-items: center; gap: 4px; }
  .topics svg { width: 15px; height: 15px; stroke: var(--ink); fill: none; stroke-width: 1.6; }

  .book {
    left: 800px; top: 184px; width: 318px;
    text-align: center;
    font-weight: 500; font-size: 23px; color: var(--white); letter-spacing: .5px;
  }
  .web {
    left: 806px; top: 215px;
    display: flex; align-items: center; gap: 8px;
    font-weight: 700; font-size: 15px; color: var(--ink);
  }
  .web svg { width: 18px; height: 18px; stroke: var(--ink); fill: none; stroke-width: 1.4; }

  .phone {
    left: 612px; top: 248px;
    display: flex; align-items: center; gap: 26px;
    font-family: "Roboto", Arial, sans-serif; font-weight: 700;
    font-size: 54px; color: var(--sun-yellow);
  }
  .phone svg { width: 42px; height: 42px; }

  .brand {
    left: 1165px; top: 140px; width: 160px;
    display: flex; flex-direction: column; align-items: center; gap: 10px;
  }
  .brand-mark { width: 34px; height: 34px; border-radius: 50%; background: var(--summer-orange); }
  .brand-name {
    font-weight: 700; font-size: 16px; line-height: 21px;
    color: var(--brand-brown); text-align: center; letter-spacing: .5px;
  }
</style>
</head>
<body>
  <section class="banner" aria-label="Heat stroke warning banner">
    <svg class="banner-shapes" viewBox="0 0 1335 320" width="1335" height="320" aria-hidden="true">
      <defs>
        <linearGradient id="photo-fill" x1="0" y1="0" x2="0" y2="1">
          <stop offset="0" stop-color="var(--photo-top)"/>
          <stop offset="1" stop-color="var(--photo-bottom)"/>
        </linearGradient>
      </defs>
      <polygon points="1207,0 1222,0 1136,320 1121,320" fill="var(--sun-yellow)"/>
      <polygon points="0,0 637,0 551,320 0,320" fill="var(--sun-yellow)"/>
      <polygon points="637,0 822,0 736,320 551,320" fill="var(--summer-orange)"/>
      <polygon points="812,20 1315,20 1300,78 797,78" fill="var(--sun-yellow)"/>
      <polygon points="555,250 1135,250 1118,308 538,308" fill="var(--ink)"/>
      <polygon points="800,183 1130,183 1118,243 788,243" fill="var(--summer-orange)"/>
      <polygon points="22,18 597,18 522,302 22,302" fill="var(--summer-orange)"/>
    </svg>

    <svg class="banner-shapes" viewBox="0 0 1335 320" width="1335" height="320" role="img" aria-label="Photo: smiling woman hugging a golden retriever on a sunny beach">
      <polygon points="27,24 589,24 517,296 27,296" fill="url(#photo-fill)"/>
    </svg>

    <div class="text question">Is your Dog</div>

    <div class="text symptom" style="left:622px;top:93px">
      <svg viewBox="0 0 16 16"><ellipse cx="8" cy="11" rx="4" ry="3.2"/><circle cx="3" cy="6.5" r="1.6"/><circle cx="6" cy="3.5" r="1.6"/><circle cx="10" cy="3.5" r="1.6"/><circle cx="13" cy="6.5" r="1.6"/></svg>Panting</div>
    <div class="text symptom" style="left:612px;top:127px">
      <svg viewBox="0 0 16 16"><ellipse cx="8" cy="11" rx="4" ry="3.2"/><circle cx="3" cy="6.5" r="1.6"/><circle cx="6" cy="3.5" r="1.6"/><circle cx="10" cy="3.5" r="1.6"/><circle cx="13" cy="6.5" r="1.6"/></svg>Loosing Breath</div>
    <div class="text symptom" style="left:603px;top:161px">
      <svg viewBox="0 0 16 16"><ellipse cx="8" cy="11" rx="4" ry="3.2"/><circle cx="3" cy="6.5" r="1.6"/><circle cx="6" cy="3.5" r="1.6"/><circle cx="10" cy="3.5" r="1.6"/><circle cx="13" cy="6.5" r="1.6"/></svg>Not Eating</div>
    <div class="text symptom" style="left:594px;top:195px">
      <svg viewBox="0 0 16 16"><ellipse cx="8" cy="11" rx="4" ry="3.2"/><circle cx="3" cy="6.5" r="1.6"/><circle cx="6" cy="3.5" r="1.6"/><circle cx="10" cy="3.5" r="1.6"/><circle cx="13" cy="6.5" r="1.6"/></svg>Restless?</div>

    <h1 class="text headline">Prevent a Heat Stroke !</h1>
    <p class="text tagline" style="left:825px;top:87px">Lets get together and help your loving dog</p>
    <p class="text tagline" style="left:820px;top:105px">strive this Hot Summer !</p>

    <p class="text get-to-know">Get to know:</p>
    <div class="text topics">
      <span><svg viewBox="0 0 16 16"><path d="M8 2 L15 14 H1 Z"/><path d="M8 6.5 V10 M8 11.5 V12.5"/></svg>Precautions</span>
      <span><svg viewBox="0 0 16 16"><path d="M5 5 A3 3 0 1 1 8 8 V10.5 M8 12.5 V13.8"/></svg>Symptoms</span>
      <span><svg viewBox="0 0 16 16"><path d="M5.5 11 A5 5 0 1 1 10.5 11 V13 H5.5 Z M6 15 H10"/></svg>Solutions</span>
    </div>

    <div class="text book">BOOK ONLINE NOW</div>
    <div class="text web">
      <svg viewBox="0 0 18 18"><circle cx="9" cy="9" r="7.5"/><ellipse cx="9" cy="9" rx="3.4" ry="7.5"/><path d="M1.5 9 H16.5 M3 5 H15 M3 13 H15"/></svg>www.maplecourtpethospital.com.au</div>

    <div class="text phone">
      <svg viewBox="0 0 42 42"><circle cx="21" cy="21" r="18" fill="none" stroke="var(--sun-yellow)" stroke-width="3"/><path d="M14 11 l5 -1 3 7 -3 2 q2 5 6 7 l2 -3 7 3 -1 5 q-3 2 -7 1 q-10 -4 -13 -14 q-1 -4 1 -7z" fill="var(--sun-yellow)"/></svg>
      <span>02 6555 0148</span>
    </div>

    <div class="text brand">
      <span class="brand-mark"></span>
      <p class="brand-name">MAPLECOURT PET<br>HOSPITAL</p>
    </div>
  </section>
</body>
</html>
```